Real Estate Investment Company Needs A Business Card Designed

I need a business card designed for my use. We are a real estate investment company based in Omaha, Nebraska that specializes in buying, rehabbing and selling single family and multifamily properties. Would love designs that incorporate our logo and colors

Industry/Entity Type

Business

Contact Information for Business Card

Marlow Pettigrew | President & CEO
4837 North 52nd Avenue, Ste 200
Omaha, NE 68214
(402) 555-7428
marlow@quillfenhomes.example
www.QuillfenHomes.example

Font styles to use
Serif

Colors
0255a3
3276b5

Requirements
Must have
• Our logo

```html
<!DOCTYPE html>
<html lang="en">
<head>
<meta charset="utf-8">
<title>Quillfen Homes – Business Card</title>
<link href="https://fonts.googleapis.com/css2?family=Questrial&family=Arimo:wght@400;700&display=swap" rel="stylesheet">
<style>
  :root {
    --brand-blue: #0255a3;
    --brand-blue-light: #3276b5;
    --panel-blue-dark: #0b4f9e;
    --strip-grey: #b9babc;
    --strip-grey-light: #d4d5d7;
    --name-tan: #c9b9a0;
    --ink-white: #ffffff;
    --card-white: #ffffff;
    --faint-circle: #e6ecf6;
    --stage: #eceef1;
  }
  * { box-sizing: border-box; margin: 0; padding: 0; }
  html, body { width: 1200px; height: 785px; overflow: hidden; }
  body {
    background: var(--stage);
    display: flex;
    align-items: center;
    justify-content: center;
    gap: 40px;
    font-family: "Arimo", Arial, sans-serif;
  }
  .card {
    position: relative;
    width: 540px;
    height: 309px;
    background: var(--card-white);
    overflow: hidden;
    box-shadow: 0 6px 18px rgba(0,0,0,0.12);
  }

  /* ---------- front ---------- */
  .front-decor {
    position: absolute;
    left: 50%; top: 50%;
    width: 360px; height: 360px;
    transform: translate(-50%, -50%);
    border-radius: 50%;
    border: 34px solid var(--faint-circle);
  }
  .front-brand {
    position: absolute;
    left: 0; right: 0; top: 72px;
    display: flex;
    flex-direction: column;
    align-items: center;
    gap: 14px;
  }
  .brand-dot {
    flex: none;
    border-radius: 50%;
    background: var(--brand-blue);
  }
  .front-brand .brand-dot { width: 96px; height: 96px; }
  .brand-name {
    font-family: "Questrial", Arial, sans-serif;
    color: var(--brand-blue);
    letter-spacing: 1px;
    text-transform: uppercase;
  }
  .front-brand .brand-name { font-size: 28px; }

  /* ---------- back ---------- */
  .back-brand {
    position: absolute;
    left: 36px; top: 22px;
    display: flex;
    align-items: center;
    gap: 18px;
  }
  .back-brand .brand-dot { width: 96px; height: 96px; }
  .back-brand .brand-name { font-size: 30px; }

  .info-panel {
    position: absolute;
    left: 182px; top: 134px; right: 0; bottom: 0;
    background: linear-gradient(120deg, var(--brand-blue-light) 0%, var(--brand-blue) 55%, var(--panel-blue-dark) 100%);
    padding: 12px 0 0 24px;
    color: var(--ink-white);
  }
  .icon-strip {
    position: absolute;
    left: 0; top: 150px; width: 172px; bottom: 0;
    background: linear-gradient(180deg, var(--strip-grey-light), var(--strip-grey));
  }
  .icon-list {
    position: absolute;
    right: 8px; top: 48px;
    display: flex;
    flex-direction: column;
    gap: 3px;
  }
  .icon-list svg { width: 16px; height: 16px; display: block; fill: var(--brand-blue); }

  .person-name {
    font-size: 18px;
    line-height: 22px;
    color: var(--name-tan);
    font-weight: 700;
  }
  .person-title {
    font-size: 14px;
    line-height: 18px;
    opacity: 0.9;
  }
  .contact-list {
    list-style: none;
    margin-top: 10px;
    font-size: 13px;
    line-height: 19px;
  }
</style>
</head>
<body>

  <section class="card card-front" aria-label="Card front">
    <div class="front-decor" aria-hidden="true"></div>
    <div class="front-brand">
      <span class="brand-dot" aria-hidden="true"></span>
      <span class="brand-name">Quillfen Homes</span>
    </div>
  </section>

  <section class="card card-back" aria-label="Card back">
    <div class="back-brand">
      <span class="brand-dot" aria-hidden="true"></span>
      <span class="brand-name">Quillfen Homes</span>
    </div>

    <div class="icon-strip">
      <div class="icon-list" aria-hidden="true">
        <svg viewBox="0 0 16 16"><path d="M4 1.5 6 4.5 4.8 6a8 8 0 0 0 5.2 5.2L11.5 10l3 2-1.3 2.3C7.5 14 2 8.5 1.7 2.8Z"/></svg>
        <svg viewBox="0 0 16 16"><path d="M1 3.5h14v9H1Zm1.4 1 5.6 4.3 5.6-4.3Zm-.4 1.3v5.7h12V5.8L8 10.2Z" fill-rule="evenodd"/></svg>
        <svg viewBox="0 0 16 16"><path d="M8 1a7 7 0 1 0 0 14A7 7 0 0 0 8 1Zm0 1.3c.9.9 1.6 2.4 1.8 4.2H6.2C6.4 4.7 7.1 3.2 8 2.3Zm-3.1 4.2H2.4a5.7 5.7 0 0 1 3.7-4c-.7 1-1.1 2.5-1.2 4Zm-2.5 1.3h2.5c.1 1.5.5 3 1.2 4a5.7 5.7 0 0 1-3.7-4Zm3.8 0h3.6c-.2 1.8-.9 3.3-1.8 4.2-.9-.9-1.6-2.4-1.8-4.2Zm4.9 0h2.5a5.7 5.7 0 0 1-3.7 4c.7-1 1.1-2.5 1.2-4Zm0-1.3c-.1-1.5-.5-3-1.2-4a5.7 5.7 0 0 1 3.7 4Z"/></svg>
        <svg viewBox="0 0 16 16"><path d="M8 1.5 15 8h-2v6.5H9.5V10h-3v4.5H3V8H1Z"/></svg>
      </div>
    </div>

    <div class="info-panel">
      <p class="person-name">Marlow Pettigrew</p>
      <p class="person-title">President &amp; CEO</p>
      <ul class="contact-list">
        <li>(402) 555-7428</li>
        <li>marlow@quillfenhomes.example</li>
        <li>www.QuillfenHomes.example</li>
        <li>4837 North 52nd Avenue, Ste 200</li>
        <li>Omaha, NE 68214</li>
      </ul>
    </div>
  </section>

</body>
</html>
```